Service Proposal brochure

I have a list of services, references and details I can provide to create the service proposal from.

Target Market(s)

Project Managers in the Construction/Electrical Field Industry

Industry/Entity Type

Construction/Electrical Industry

Font styles to use
Serif

Colors
0054AA
0677BA
7BADD7
CADEEF
E8F1F8
FFF300
FFF600
FEFA6F
FFFEC7
FFFEE8

Requirements
Must have
• High vocabulary
Nice to have
• Creativity in the details of service work and layout of the brochure
Should not have
• So much wording that it becomes boring for the consumer

```html
<!DOCTYPE html>
<html lang="en">
<head>
<meta charset="utf-8">
<title>Service Proposal – References</title>
<link href="https://fonts.googleapis.com/css2?family=Poppins:wght@400;600;700&display=swap" rel="stylesheet">
<style>
:root{
  --navy:#1a4fa0;
  --blue:#0a7bc2;
  --deep:#1452a8;
  --sky:#3f8fd0;
  --line:#b8d0ea;
  --yellow:#fff300;
  --gray:#6b6f75;
  --stage:#e6e8eb;
}
*{margin:0;padding:0;box-sizing:border-box}
html,body{width:1200px;height:2824px;overflow:hidden;background:var(--stage);font-family:'Poppins',sans-serif}
.page{
  position:absolute;left:40px;top:620px;width:941px;height:1332px;
  transform:scale(1.1902);transform-origin:0 0;overflow:hidden;
  background:linear-gradient(160deg,#f4f5f7 0%,#e4e6e9 35%,#f5f6f8 60%,#e1e3e6 100%);
  box-shadow:0 10px 40px rgba(0,0,0,.25);
}
.swoosh{position:absolute;inset:0}
.spine{position:absolute;left:179px;top:100px;width:12px;height:1240px;background:var(--line);opacity:.8}
.ref-frame{
  position:absolute;left:44px;top:103px;width:854px;height:344px;
  border:1.5px solid #cfd3d8;border-radius:14px;background:rgba(255,255,255,.55);
}
.ref-title{position:absolute;left:80px;top:122px;font-size:38px;font-weight:700;color:var(--navy);text-decoration:underline}
.ref-org{position:absolute;left:80px;top:207px;font-size:19px;font-weight:600;color:#0a6bb3;text-decoration:underline}
.ref{position:absolute;left:80px;font-size:19px;line-height:26px;color:var(--sky)}
.ref b{color:var(--navy);font-weight:700}
.ref .contact{display:block;color:var(--gray);padding-left:10px}
.ref .indent{display:block;padding-left:163px}
.connector{position:absolute;left:0;top:0}
.card-frame{position:absolute;border:1.5px dashed #a9c4e3;border-radius:8px}
.card{position:absolute;border-radius:8px;color:#fff;padding:28px 14px 0 14px;font-size:18px;line-height:24px}
.card .org{color:var(--yellow);font-weight:700;font-size:19px;line-height:23px;margin-bottom:20px}
.card b{font-weight:700}
.card-a{background:var(--blue)}
.card-b{background:var(--deep)}
.services{
  position:absolute;left:556px;top:312px;width:400px;height:1040px;
  background:rgba(246,247,249,.93);border-radius:30px 0 0 50px;
}
.services-head{height:66px;background:linear-gradient(90deg,#1168b8,#0a5fae);border-radius:30px 0 0 0;padding:12px 0 0 36px}
.services-head h2{font-size:32px;font-weight:700;color:var(--yellow);text-decoration:underline}
.service-list{list-style:none;padding:21px 16px 0 36px;display:flex;flex-direction:column;gap:21px}
.service-list li{font-size:17.5px;line-height:21px;color:var(--sky)}
.service-list b{color:var(--navy);font-weight:600}
.service-list .pad{padding-left:8px}
</style>
</head>
<body>
<main class="page">
  <svg class="swoosh" width="941" height="1332" viewBox="0 0 941 1332" aria-hidden="true">
    <path d="M0 90 C250 20 600 10 941 60 L941 0 L0 0Z" fill="#fff" opacity=".5"/>
    <path d="M0 260 C300 120 650 80 941 140" stroke="#fff" stroke-width="40" fill="none" opacity=".35"/>
    <path d="M0 700 C300 520 600 420 941 380" stroke="#fff" stroke-width="90" fill="none" opacity=".3"/>
  </svg>
  <div class="spine"></div>

  <section class="ref-frame"></section>
  <h1 class="ref-title">References:</h1>
  <p class="ref-org">Redhill Crest University</p>
  <p class="ref" style="top:246px"><b>*DANA WHITLOCK -</b> Director of Campus Engineering -<span class="contact">dwhitlock@rcu.edu - 909-555-0142</span></p>
  <p class="ref" style="top:334px"><b>*MARCUS ELLERY-</b> Construction &amp; Wayfinding<span class="indent">Senior Projector Manger</span><span class="contact">mellery@rcu.edu&nbsp; (951)-555-0176</span></p>

  <svg class="connector" width="941" height="1332" aria-hidden="true">
    <polyline points="316,740 386,740 386,832" fill="none" stroke="var(--line)" stroke-width="12"/>
    <polyline points="386,1018 386,1050 195,1050 195,1080" fill="none" stroke="var(--line)" stroke-width="12"/>
  </svg>

  <div class="card-frame" style="left:44px;top:495px;width:282px;height:287px"></div>
  <article class="card card-a" style="left:54px;top:507px;width:262px;height:265px">
    <p class="org">Pine Hollow Valley<br>Water District</p>
    <p><b>Owen Castellan-</b><br>Director of Operations</p>
    <p style="margin-top:24px">o.castellan@phvwd.org<br>(951) 555-0193- ext.417</p>
  </article>

  <div class="card-frame" style="left:245px;top:830px;width:282px;height:198px"></div>
  <article class="card card-b" style="left:256px;top:840px;width:261px;height:178px;padding-top:18px">
    <p class="org" style="margin-bottom:14px">Halvorsen<br>Engineering</p>
    <p><b>Owen Castellan-</b><br>Plant &amp;Facilities<br>Maintenance Director</p>
  </article>

  <div class="card-frame" style="left:44px;top:1077px;width:317px;height:222px"></div>
  <article class="card card-a" style="left:54px;top:1089px;width:297px;height:200px;padding-top:20px">
    <p class="org" style="margin-bottom:14px">Cedar Mesa School<br>District</p>
    <p><b>Rafael Montoya -</b><br>Maintenance Supervisor<br>rafael_montoya@cmsd.us<br>(909) 555-0168</p>
  </article>

  <aside class="services">
    <div class="services-head"><h2>Service’s include:</h2></div>
    <ul class="service-list">
      <li><b>*Power-</b> Upgrade/ Additional</li>
      <li><b>*Lighting-</b> Upgrade/ additional/<br><span class="pad">retrofits</span></li>
      <li><b>*Remodels</b></li>
      <li><b>*Design Build &amp; Design assist</b></li>
      <li><b>*Medium voltage</b></li>
      <li><b>*New equipment</b></li>
      <li><b>*Voltaris Battery packs</b></li>
      <li><b>*Generators and Automatic<br><span class="pad">Transfer Switches</span></b></li>
      <li><b>*Preventive Maintenance and<br><span class="pad">Testing</span></b>&nbsp;&nbsp;&nbsp;&nbsp;(ETCA 2 Certified)</li>
      <li><b>*Arch Flash/Coordination Study</b></li>
      <li><b>*Title 24 commissioning and<br>acceptance</b></li>
      <li><b>*Fire Alarm –</b> Quiet Sentry, Brenner,<br>Flare-Tek</li>
      <li><b>*Security(Intrusion) –</b> Brenner, KSL,<br>Corvane, AlertNet.com</li>
      <li><b>*Security(Access Control) –</b><br>Kordtech &amp; Vireo</li>
      <li><b>*Security(Cameras) –</b> Lumivue, EC<br>Livetime, Brenner</li>
      <li><b>*Public Address –</b> Walsera &amp; Astra<br>AED</li>
      <li><b>*Structured Cable –</b> Levion,<br>Birch-Tek</li>
    </ul>
  </aside>
</main>
</body>
</html>
```